Vantorel Business Card

I want a business card for me and my employees.
On one side it must be in Greek and on the other side in English. The color must much the one of the logo

Target Market(s)

Customers that are looking for security and antipiracy advisors

Contact Information for Business Card

Title, Email, Phone, website , Mobile Address Zip code, city and country

Requirements
Must have
• The colors of our logo (the blue ones)

```html
<!DOCTYPE html>
<html lang="en">
<head>
<meta charset="UTF-8">
<title>Vantorel Advisory – Business Cards</title>
<link rel="stylesheet" href="https://fonts.googleapis.com/css2?family=Montserrat:wght@400;500;700&display=swap">
<style>
  :root {
    --backdrop: #2e2e31;
    --card-deep: #25235f;
    --card-mid: #2f2b7c;
    --ink: #ffffff;
    --rule: rgba(255, 255, 255, 0.55);
    --mark-fill: rgba(255, 255, 255, 0.06);
  }
  * { margin: 0; padding: 0; box-sizing: border-box; }
  html, body {
    width: 1200px; height: 1200px; overflow: hidden;
    background: var(--backdrop);
    font-family: "Montserrat", Arial, sans-serif;
    color: var(--ink);
  }
  .sheet {
    position: relative; width: 1200px; height: 1200px;
    display: flex; flex-direction: column; align-items: center; justify-content: center; gap: 70px;
  }
  .card {
    position: relative; width: 840px; height: 480px;
    border-radius: 34px;
    background: linear-gradient(135deg, var(--card-mid) 0%, var(--card-deep) 100%);
    box-shadow: 0 18px 40px rgba(0, 0, 0, 0.45);
    overflow: hidden;
  }
  .backdrop-shape {
    position: absolute; left: 300px; top: 50px; width: 230px; height: 380px;
    background: var(--mark-fill); border-radius: 6px;
  }
  .brand {
    position: absolute; left: 190px; top: 92px;
    display: flex; align-items: center; gap: 22px;
  }
  .brand-square { width: 70px; height: 70px; border: 0 solid; background: var(--ink); }
  .brand-name {
    font-weight: 700; font-size: 46px; line-height: 1.05; letter-spacing: 1px;
    text-transform: uppercase; color: var(--ink);
  }
  .rule { position: absolute; background: var(--rule); }
  .rule-top { left: 400px; top: 222px; width: 380px; height: 1.5px; }
  .rule-name { left: 80px; top: 300px; width: 340px; height: 1.5px; }
  .rule-divider { left: 440px; top: 250px; width: 1.5px; height: 150px; }
  .person { position: absolute; left: 80px; top: 335px; font-size: 26px; line-height: 1.15; text-transform: uppercase; }
  .person-name { font-weight: 700; }
  .person-title { font-weight: 500; }
  .card-el .person-name, .card-el .person-title { font-weight: 400; }
  .contacts { position: absolute; left: 475px; top: 250px; list-style: none; font-size: 19px; line-height: 1.35; }
  .contacts li { display: flex; align-items: flex-start; gap: 12px; }
  .contacts svg { width: 20px; height: 20px; margin-top: 3px; flex: none; fill: var(--ink); }
  .contacts .indent { padding-left: 32px; }
</style>
</head>
<body>
<main class="sheet">

  <section class="card card-el" lang="el">
    <div class="backdrop-shape"></div>
    <div class="brand">
      <span class="brand-square"></span>
      <span class="brand-name">Vantorel<br>Advisory</span>
    </div>
    <span class="rule rule-top"></span>
    <span class="rule rule-name"></span>
    <span class="rule rule-divider"></span>
    <div class="person">
      <p class="person-name">Πληρες Ονομα</p>
      <p class="person-title">Τιτλος</p>
    </div>
    <ul class="contacts">
      <li><svg viewBox="0 0 24 24"><path d="M6.6 10.8a15 15 0 0 0 6.6 6.6l2.2-2.2c.3-.3.7-.4 1-.2 1.1.4 2.3.6 3.6.6.6 0 1 .4 1 1V20c0 .6-.4 1-1 1A17 17 0 0 1 3 4c0-.6.4-1 1-1h3.5c.6 0 1 .4 1 1 0 1.3.2 2.5.6 3.6.1.3 0 .7-.2 1z"/></svg>(000) 000 0000</li>
      <li><svg viewBox="0 0 24 24"><path d="M2 5h20v14H2zm2 2v.5l8 5 8-5V7zm0 3v7h16v-7l-8 5z"/></svg>email@company.com</li>
      <li><svg viewBox="0 0 24 24"><path d="M12 2a10 10 0 1 0 0 20 10 10 0 0 0 0-20zm6.9 9h-3a15 15 0 0 0-1.3-6A8 8 0 0 1 18.9 11zM12 4c.9 1.2 1.8 3.6 2 7h-4c.2-3.4 1.1-5.8 2-7zM9.4 5a15 15 0 0 0-1.3 6h-3A8 8 0 0 1 9.4 5zM5.1 13h3a15 15 0 0 0 1.3 6A8 8 0 0 1 5.1 13zM12 20c-.9-1.2-1.8-3.6-2-7h4c-.2 3.4-1.1 5.8-2 7zm2.6-1a15 15 0 0 0 1.3-6h3a8 8 0 0 1-4.3 6z"/></svg>www.company.com</li>
      <li><svg viewBox="0 0 24 24"><path d="M12 2a7 7 0 0 0-7 7c0 5 7 13 7 13s7-8 7-13a7 7 0 0 0-7-7zm0 9.5a2.5 2.5 0 1 1 0-5 2.5 2.5 0 0 1 0 5z"/></svg>Οδός 123, 000</li>
      <li class="indent">Η πόλη σας, 00000-000</li>
    </ul>
  </section>

  <section class="card card-en" lang="en">
    <div class="backdrop-shape"></div>
    <div class="brand">
      <span class="brand-square"></span>
      <span class="brand-name">Vantorel<br>Advisory</span>
    </div>
    <span class="rule rule-top"></span>
    <span class="rule rule-name"></span>
    <span class="rule rule-divider"></span>
    <div class="person">
      <p class="person-name">Full Name</p>
      <p class="person-title">Title</p>
    </div>
    <ul class="contacts">
      <li><svg viewBox="0 0 24 24"><path d="M6.6 10.8a15 15 0 0 0 6.6 6.6l2.2-2.2c.3-.3.7-.4 1-.2 1.1.4 2.3.6 3.6.6.6 0 1 .4 1 1V20c0 .6-.4 1-1 1A17 17 0 0 1 3 4c0-.6.4-1 1-1h3.5c.6 0 1 .4 1 1 0 1.3.2 2.5.6 3.6.1.3 0 .7-.2 1z"/></svg>(000) 000 0000</li>
      <li><svg viewBox="0 0 24 24"><path d="M2 5h20v14H2zm2 2v.5l8 5 8-5V7zm0 3v7h16v-7l-8 5z"/></svg>email@company.com</li>
      <li><svg viewBox="0 0 24 24"><path d="M12 2a10 10 0 1 0 0 20 10 10 0 0 0 0-20zm6.9 9h-3a15 15 0 0 0-1.3-6A8 8 0 0 1 18.9 11zM12 4c.9 1.2 1.8 3.6 2 7h-4c.2-3.4 1.1-5.8 2-7zM9.4 5a15 15 0 0 0-1.3 6h-3A8 8 0 0 1 9.4 5zM5.1 13h3a15 15 0 0 0 1.3 6A8 8 0 0 1 5.1 13zM12 20c-.9-1.2-1.8-3.6-2-7h4c-.2 3.4-1.1 5.8-2 7zm2.6-1a15 15 0 0 0 1.3-6h3a8 8 0 0 1-4.3 6z"/></svg>www.company.com</li>
      <li><svg viewBox="0 0 24 24"><path d="M12 2a7 7 0 0 0-7 7c0 5 7 13 7 13s7-8 7-13a7 7 0 0 0-7-7zm0 9.5a2.5 2.5 0 1 1 0-5 2.5 2.5 0 0 1 0 5z"/></svg>123 Name Street, 000</li>
      <li class="indent">Your City, 00000-000</li>
    </ul>
  </section>

</main>
</body>
</html>
```